Architectural, Engineering and Design Build

Tavonex4.com
Veteran Disabled Certified company is doing business in Architecture, Engineer and Design build - look simialr websites and come up with design follow following website
https://dorsey-kalbin.example/
https://www.velmonteam.example/
https://www.pirnoqa.example/contract-vehicles/service-disabled-veteran-owned-small-business-sdvosb/
https://www.corbelhubnet.example/about/sdvosb/

Target Market(s)

US - Defense and Federal Government

Industry/Entity Type

Colors
0054AA
0677BA
7BADD7
CADEEF
E8F1F8

Requirements
Must have
• Army, American patriotism , Buildings, construction, architecture, engineering
Nice to have
• I need to attract federal government agencies and Defense

```html
<!DOCTYPE html>
<html lang="en">
<head>
<meta charset="utf-8">
<title>Tavonex4 — Architecture, Engineering and Design Build</title>
<link href="https://fonts.googleapis.com/css2?family=Catamaran:wght@400;600;700;800&family=Lato:wght@400;700&display=swap" rel="stylesheet">
<style>
:root{
  --blue:#0054AA;
  --blue-mid:#0677BA;
  --blue-soft:#7BADD7;
  --blue-pale:#CADEEF;
  --blue-mist:#E8F1F8;
  --ink:#2b2f36;
  --text:#444a52;
  --grey-bg:#f3f3f4;
  --footer:#262a33;
  --white:#ffffff;
}
*{margin:0;padding:0;box-sizing:border-box}
html,body{width:1200px;height:3675px;overflow:hidden}
body{font-family:"Lato",sans-serif;color:var(--text);background:var(--white);position:relative}
.abs{position:absolute}
h1,h2,h3,.display{font-family:"Catamaran",sans-serif}

/* hero */
.hero{position:absolute;left:0;top:0;width:1200px;height:675px;
  background:linear-gradient(180deg,#1d2f5a 0%,#3a4c72 35%,#6a6f7c 70%,#8a8681 100%)}
.hero-photo{position:absolute;inset:0;
  background:radial-gradient(ellipse at 85% 40%,rgba(190,185,175,.45),transparent 55%),radial-gradient(ellipse at 55% 30%,rgba(170,60,60,.25),transparent 20%),linear-gradient(180deg,rgba(10,30,80,.55),rgba(20,30,60,.25))}
.brand{font-family:"Catamaran",sans-serif;font-weight:800;color:var(--white);letter-spacing:3px;white-space:nowrap}
.hero .brand{left:126px;top:34px;font-size:56px;line-height:1}
.nav{right:104px;top:54px;display:flex;gap:38px;font-family:"Catamaran",sans-serif;font-weight:700;font-size:17px;color:var(--white)}
.hero-title{left:0;width:1200px;top:296px;text-align:center;color:var(--white);font-weight:700;font-size:38px;line-height:58px}
.btn-outline{display:flex;align-items:center;justify-content:center;border:2px solid var(--white);color:var(--white);font-family:"Catamaran",sans-serif;font-weight:700;font-size:16px;border-radius:3px}
.hero .btn-outline{left:509px;top:438px;width:186px;height:51px}

/* who we are */
.who-title{left:113px;top:788px;font-family:"Catamaran",sans-serif;font-size:38px;color:var(--ink);font-weight:400}
.who-title b{font-weight:700}
.who-rule{left:115px;top:848px;width:70px;height:3px;background:var(--blue)}
.who-text{left:447px;top:772px;width:700px;font-size:19.5px;line-height:36px;color:#444;white-space:nowrap}

/* services */
.services{left:0;top:985px;width:597px;height:610px;background:var(--blue-mist)}
.service{position:absolute;left:112px;width:400px}
.service svg{position:absolute;left:0;top:38px}
.service h3{position:absolute;left:86px;top:0;font-size:23px;font-weight:700;color:var(--ink)}
.service p{position:absolute;left:86px;top:40px;width:320px;font-size:16px;line-height:27px;color:#444;white-space:nowrap}
.cta-photo{left:597px;top:985px;width:603px;height:610px;
  background:linear-gradient(180deg,#8a8f96 0%,#c99a55 35%,#d8822e 55%,#6b4a2a 80%,#3d3a38 100%)}
.cta-title{left:643px;top:1378px;font-size:29px;font-weight:700;color:var(--white)}
.btn-solid{display:flex;align-items:center;justify-content:center;background:var(--blue-mid);color:var(--white);font-family:"Catamaran",sans-serif;font-size:22px}
.cta-btn{left:649px;top:1442px;width:183px;height:49px}

/* certification */
.cert{left:0;top:1595px;width:1200px;height:510px;background:#f6f6f7}
.cert-photo{left:0;top:1615px;width:670px;height:490px;background:radial-gradient(ellipse at 20% 70%,#d9dadc,transparent 60%);opacity:.9}
.cert-title{left:114px;top:1690px;font-family:"Catamaran",sans-serif;font-size:37px;line-height:48px;color:#333;font-weight:400}
.cert-text{font-size:17.5px;line-height:28px;color:#555;white-space:nowrap}
.cert-p1{left:115px;top:1800px}
.cert-sub{left:114px;top:1908px;font-family:"Catamaran",sans-serif;font-size:23px;font-weight:600;color:#222}
.cert-p2{left:115px;top:1951px}
.badge{left:775px;top:1710px;width:305px;height:290px;border-radius:50%;background:var(--blue-pale)}

/* projects */
.projects{left:0;top:2105px;width:1200px;height:456px;background:var(--blue)}
.proj-watermark{left:48px;top:2150px;font-family:"Catamaran",sans-serif;font-weight:800;font-size:190px;letter-spacing:22px;color:transparent;-webkit-text-stroke:2px rgba(255,255,255,.07);line-height:1}
.proj-label{left:52px;top:2194px;display:flex;align-items:center;gap:14px;color:var(--white);font-family:"Catamaran",sans-serif;font-weight:700;font-size:21px}
.proj-label i{display:block;width:22px;height:3px;background:var(--white)}
.proj-title{left:52px;top:2232px;color:var(--white);font-size:45px;font-weight:700;line-height:59px}
.proj-text{left:504px;top:2242px;color:var(--white);font-size:16.5px;line-height:28px;white-space:nowrap}
.lower-band{left:0;top:2561px;width:1200px;height:821px;background:var(--grey-bg)}
.tile{top:2421px;width:209px;height:266px}
.tile-1{left:245px;background:linear-gradient(160deg,#9fc1e4,#2a4f78 55%,#0e1e30)}
.tile-2{left:475px;background:linear-gradient(180deg,#1a4f9a 0%,#4f7bb5 45%,#c9a05a 70%,#6c88a8 100%)}
.tile-3{left:711px;background:linear-gradient(180deg,#dfe5ec 0%,#8aa0aa 45%,#2f6f5a 80%,#5a6a60 100%)}
.tile-4{left:940px;background:linear-gradient(180deg,#f0f0f0 0%,#c7c9cb 55%,#e2e2e2 100%)}
.tile-caption{position:absolute;left:18px;bottom:26px;color:var(--white);font-family:"Catamaran",sans-serif;font-weight:700;font-size:13px;line-height:28px}
.tile-caption span{display:block;border-left:3px solid var(--blue-mid);padding-left:10px}
.view-more{left:547px;top:2728px;width:164px;height:45px;border:2px solid var(--blue);border-radius:2px;display:flex;align-items:center;justify-content:center;color:var(--blue);font-family:"Catamaran",sans-serif;font-weight:700;font-size:16px}

/* testimonials */
.map-dots{left:150px;top:2850px;width:900px;height:490px;background:radial-gradient(ellipse at 50% 50%,rgba(200,205,212,.45),transparent 65%)}
.t-label{left:0;width:1200px;top:2891px;text-align:center;color:var(--blue-mid);font-family:"Catamaran",sans-serif;font-weight:700;font-size:12px;letter-spacing:.5px}
.t-title{left:0;width:1195px;top:2915px;text-align:center;font-family:"Catamaran",sans-serif;font-size:38px;color:#333;font-weight:400}
.t-title b{font-weight:700}
.card{top:3031px;width:465px;height:236px;background:var(--white);box-shadow:0 4px 18px rgba(0,0,0,.05)}
.card-1{left:123px}
.card-2{left:623px}
.avatar{position:absolute;left:28px;top:29px;width:94px;height:94px;border-radius:50%}
.card-1 .avatar{background:linear-gradient(160deg,#d7c8b4,#7a6a58)}
.card-2 .avatar{background:linear-gradient(160deg,#2d5f8a,#1a2530)}
.card p{position:absolute;left:154px;top:32px;font-size:12.5px;line-height:23px;color:#555;white-space:nowrap}
.card h4{position:absolute;left:154px;top:145px;font-family:"Catamaran",sans-serif;font-weight:700;font-size:17px;color:#222}
.stars{position:absolute;left:153px;top:180px}
.quote{position:absolute;right:30px;top:150px;font-family:"Catamaran",sans-serif;font-weight:800;font-size:80px;line-height:1;color:var(--blue-soft)}
.arrow{width:50px;height:50px;border-radius:50%;background:var(--white);box-shadow:0 2px 10px rgba(0,0,0,.08);display:flex;align-items:center;justify-content:center}

/* footer */
.footer{left:0;top:3382px;width:1200px;height:193px;background:var(--footer)}
.footer-brand{left:108px;top:3440px;font-size:64px;line-height:1}
.socials{left:739px;top:3458px;display:flex;gap:18px}
.socials span{display:block;width:60px;height:60px;border:2px solid #8a8e96;border-radius:50%}
.footer-bar{left:0;top:3575px;width:1200px;height:100px;background:#2e323b;border-top:1px solid #4a4e56}
.footer-links{left:99px;top:3614px;display:flex;gap:14px;color:#9ea3ab;font-size:15px}
.footer-links em{font-style:normal;color:#6d727a}
.copyright{right:76px;top:3614px;color:#9ea3ab;font-size:14.5px}
</style>
</head>
<body>

<header class="hero">
  <div class="hero-photo" role="img" aria-label="Capitol dome with the national flag flying against a blue sky"></div>
  <div class="abs brand">TAVONEX4</div>
  <nav class="abs nav"><span>ABOUT</span><span>SERVICES</span><span>PROJECTS</span><span>CONTACT US</span></nav>
  <h1 class="abs hero-title">Veteran Disabled Certified Company<br>Owned Business</h1>
  <a class="abs btn-outline">GET STARTED NOW</a>
</header>

<h2 class="abs who-title">Who <b>We Are</b></h2>
<div class="abs who-rule"></div>
<p class="abs who-text">Who We Are We only invest in post-product, post-revenue Enterprise IT<br>startups. Usually, this means you're at Seed Extension to Series A stage<br>Lorem Ipsum is simply dummy text of the printing and type setting ind<br>ustry has been the industry’s standard.</p>

<section class="abs services">
  <div class="service" style="top:80px">
    <svg width="66" height="66" viewBox="0 0 66 66" fill="none" stroke="#0677BA" stroke-width="2.4"><rect x="4" y="10" width="46" height="46" rx="2"/><path d="M4 20h8M4 30h8M4 40h8M22 50l30-30 6 6-30 30h-6z"/><path d="M44 30l6 6"/></svg>
    <h3>Architecture</h3>
    <p>Lorem ipsum is simply dummy text<br>printing typetting industry lorpsum<br>has dummy uis aute.</p>
  </div>
  <div class="service" style="top:240px">
    <svg width="70" height="70" viewBox="0 0 70 70" fill="none" stroke="#0677BA" stroke-width="2.4"><rect x="4" y="14" width="44" height="40" rx="2"/><circle cx="40" cy="16" r="9"/><circle cx="22" cy="32" r="6"/><path d="M44 38l18 18M4 46h44"/></svg>
    <h3>Engineering</h3>
    <p>Lorem ipsum is simply dummy text<br>printing typetting industry lorpsum<br>has dummy uis aute.</p>
  </div>
  <div class="service" style="top:400px">
    <svg width="66" height="66" viewBox="0 0 66 66" fill="none" stroke="#0677BA" stroke-width="2.4"><rect x="4" y="12" width="56" height="36" rx="2"/><path d="M24 48v8M40 48v8M16 58h32M30 38l20-22 6 6-20 22z"/></svg>
    <h3>Design</h3>
    <p>Lorem ipsum is simply dummy text<br>printing typetting industry lorpsum<br>has dummy uis aute.</p>
  </div>
</section>
<div class="abs cta-photo" role="img" aria-label="City skyline of high-rise towers at golden sunset"></div>
<h2 class="abs cta-title">Let’s start your next project today</h2>
<a class="abs btn-solid cta-btn">Contact Us</a>

<section class="abs cert"></section>
<div class="abs cert-photo" role="img" aria-label="Faded monument of soldiers raising the flag"></div>
<h2 class="abs cert-title">Certification for Service Disabled<br>Veteran Owned Small Business</h2>
<p class="abs cert-text cert-p1">Lorem ipsum dolor amet consectetur adipiscing eiusmod temp<br>Lorem ipsum dolor sit amet consectetur adipiscing elit<br>do eiusmod tempor incididunt ut labore et dolore.</p>
<h3 class="abs cert-sub">Next Generation Enterprises</h3>
<p class="abs cert-text cert-p2">Lorem ipsum dolor amet consectetur adipiscing eiusmod temp<br>Lorem ipsum dolor sit amet consectetur</p>
<div class="abs badge" role="img" aria-label="Certification badge"></div>

<section class="abs projects"></section>
<div class="abs proj-watermark">PROJECTS</div>
<div class="abs proj-label"><i></i>LATEST PROJECTS</div>
<h2 class="abs proj-title">Let’s Explore Our<br>Recent Works</h2>
<p class="abs proj-text">The right software solution by itself will not run your business. It takes a team to do that.<br>In addition to selecting the best cloud solution on the market, it takes smart and<br>dedicated people remaining essentially unchanged.</p>
<div class="abs lower-band"></div>
<div class="abs tile tile-1" role="img" aria-label="Glass office tower seen from below">
  <div class="tile-caption">Commercial&nbsp; Residential<span>Modern House</span></div>
</div>
<div class="abs tile tile-2" role="img" aria-label="Curved glass concert hall lit at dusk"></div>
<div class="abs tile tile-3" role="img" aria-label="Tower crane above a building under construction"></div>
<div class="abs tile tile-4" role="img" aria-label="White architectural model on blueprints"></div>
<a class="abs view-more">VIEW MORE</a>

<div class="abs map-dots" role="img" aria-label="Dotted world map"></div>
<div class="abs t-label">TESTIMONIALS</div>
<h2 class="abs t-title">Words From <b>Clients</b></h2>
<article class="abs card card-1">
  <div class="avatar" role="img" aria-label="Client portrait"></div>
  <p>when an unknown printer took a galley of<br>type and scrambled it to make a type not<br>only five centurie when an unknown printer<br>took a galley of type</p>
  <h4>Marlo Venick</h4>
  <svg class="stars" width="84" height="14" viewBox="0 0 84 14"><g fill="#f5b800"><path id="st" d="M7 0l2 5h5l-4 3 1.5 5L7 10l-4.5 3L4 8 0 5h5z"/><use href="#st" x="17"/><use href="#st" x="34"/><use href="#st" x="51"/></g><use href="#st" x="68" fill="#999"/></svg>
  <div class="quote">”</div>
</article>
<article class="abs card card-2">
  <div class="avatar" role="img" aria-label="Client portrait"></div>
  <p>when an unknown printer took a galley of<br>type and scrambled it to make a type not<br>only five centurie when an unknown printer<br>took a galley of type</p>
  <h4>Dace Holloran</h4>
  <svg class="stars" width="84" height="14" viewBox="0 0 84 14"><g fill="#f5b800"><path id="st2" d="M7 0l2 5h5l-4 3 1.5 5L7 10l-4.5 3L4 8 0 5h5z"/><use href="#st2" x="17"/><use href="#st2" x="34"/><use href="#st2" x="51"/></g><use href="#st2" x="68" fill="#999"/></svg>
  <div class="quote">”</div>
</article>
<div class="abs arrow" style="left:54px;top:3125px"><svg width="10" height="14" viewBox="0 0 10 14" fill="none" stroke="#666" stroke-width="1.6"><path d="M8 1L2 7l6 6"/></svg></div>
<div class="abs arrow" style="left:1103px;top:3121px"><svg width="10" height="14" viewBox="0 0 10 14" fill="none" stroke="#666" stroke-width="1.6"><path d="M2 1l6 6-6 6"/></svg></div>

<footer class="abs footer"></footer>
<div class="abs brand footer-brand">TAVONEX4</div>
<div class="abs socials" aria-label="Social links"><span></span><span></span><span></span><span></span><span></span></div>
<div class="abs footer-bar"></div>
<nav class="abs footer-links"><span>Home</span><em>|</em><span>About</span><em>|</em><span>Services</span><em>|</em><span>Contact</span><em>|</em><span>About</span><em>|</em><span>Blog</span></nav>
<div class="abs copyright">Copyright © 2022. All Rights Reserved.</div>

</body>
</html>
```